Brightmoor Senior Living Marketing Brochure, Covid-19 Brochure, Introduction to our manager

We are a Senior Living Community that services Assisted living and memory care. We have a lot of New programs for Activities, Food recipes, therapy, family and resident interaction , covid free, and want to introduce this to the community and existing family members.

Target Market(s)

Harbor Point and San Diego for Brightmoor Senior Living and Memory Care of La Jolla and For Brightmoor Senior Living and Memory Care of Tarzana , San Fernando valley, tarzana, Encino , Woodland Hills Sherman oaks

Industry/Entity Type

Assisted Living

Colors
a54499
f7f3f9
ffffff
fece3e
ffc214

Requirements
Must have
• Product names for our marketing brochure , facility images per location

```html
<!DOCTYPE html>
<html lang="en">
<head>
<meta charset="utf-8">
<title>Brightmoor Senior Living Marketing Brochure</title>
<link rel="stylesheet" href="https://fonts.googleapis.com/css2?family=Cinzel:wght@500;700&family=Open+Sans:wght@400;600;700&display=swap">
<style>
  :root{
    --magenta:#a54499;
    --magenta-dark:#8a3580;
    --lilac:#f7f3f9;
    --white:#ffffff;
    --gold:#c9a23d;
    --gold-light:#fece3e;
    --gold-bright:#ffc214;
    --ink:#4a3a44;
    --stage:#e9e9ea;
  }
  *{box-sizing:border-box;margin:0;padding:0}
  html,body{width:1200px;height:2400px;overflow:hidden}
  body{background:var(--stage);font-family:"Open Sans",sans-serif;color:var(--ink);position:relative}
  .spread{position:absolute;left:50px;width:1100px;height:850px;display:flex;box-shadow:0 6px 24px rgba(0,0,0,.12)}
  .spread--outside{top:250px}
  .spread--inside{top:1300px}
  .panel{position:relative;width:366.67px;height:850px;overflow:hidden}
  .photo{position:absolute;display:block}
  .brand{display:flex;align-items:center;justify-content:center;gap:10px;font-family:"Cinzel",serif;font-weight:700;letter-spacing:3px;color:var(--magenta)}
  .brand__dot{width:16px;height:16px;border-radius:50%;background:var(--gold-bright)}
  .brand-sub{font-family:"Cinzel",serif;font-weight:500;font-size:12px;letter-spacing:3px;text-align:center;color:var(--gold)}
  h2{font-family:"Cinzel",serif;font-weight:700;font-size:20px;letter-spacing:1px}
  h3{font-family:"Open Sans",sans-serif;font-weight:700;font-size:14px;text-transform:uppercase;letter-spacing:1px}
  p{font-size:12px;line-height:1.6}

  /* outside: program flap */
  .flap{background:var(--lilac)}
  .flap__body{position:absolute;top:50px;left:36px;right:32px}
  .flap h2{color:var(--magenta);margin-bottom:14px}
  .flap p{margin-bottom:18px}
  .checklist{list-style:none}
  .checklist li{display:flex;gap:10px;align-items:flex-start;font-size:13px;line-height:1.5;margin-bottom:12px}
  .checklist svg{flex:none;margin-top:2px}
  .flap .photo{left:0;bottom:0;width:100%;height:300px}

  /* outside: back panel */
  .back{background:var(--magenta);color:var(--white)}
  .back .brand{color:var(--white);font-size:22px;margin-top:50px}
  .back .brand-sub{color:var(--gold-light);margin-top:6px}
  .back__title{text-align:center;margin:24px 20px 0;font-size:16px;white-space:nowrap}
  .back .photo{left:40px;top:230px;width:286px;height:190px;border:6px solid var(--white)}
  .back__contact{position:absolute;left:40px;right:40px;top:460px}
  .back__contact h2{color:var(--gold-light);text-align:center;margin-bottom:18px}
  .contact-line{display:flex;gap:12px;align-items:center;font-size:13px;margin-bottom:14px}
  .back__band{position:absolute;left:0;right:0;bottom:0;height:120px}

  /* outside: cover */
  .cover{background:var(--lilac)}
  .cover .brand{font-size:28px;margin-top:58px}
  .cover .brand-sub{margin-top:8px}
  .cover .photo{left:0;top:170px;width:100%;height:380px}
  .cover__shape{position:absolute;left:0;top:470px;width:100%;height:380px}
  .cover__tagline{position:absolute;left:30px;right:30px;top:640px;text-align:center;color:var(--white);font-family:"Cinzel",serif;font-weight:700;font-size:20px;letter-spacing:2px;line-height:1.4}
  .cover__subline{position:absolute;left:30px;right:30px;top:720px;text-align:center;color:var(--white);font-size:12px;letter-spacing:2px;text-transform:uppercase}

  /* inside: left */
  .programs{background:var(--gold);color:var(--white)}
  .programs__list{position:absolute;top:44px;left:32px;right:30px}
  .program{display:flex;gap:14px;margin-bottom:22px}
  .program__icon{flex:none;width:34px;height:34px;border-radius:50%;background:var(--magenta);display:flex;align-items:center;justify-content:center}
  .program h3{margin-bottom:4px}
  .program p{font-size:11.5px}
  .programs .photo{left:0;bottom:0;width:100%;height:300px}

  /* inside: middle */
  .story{background:var(--white)}
  .story__strip{position:absolute;top:30px;left:30px;right:30px;display:flex;gap:8px}
  .story__strip .thumb{flex:1;height:96px;display:block}
  .story__body{position:absolute;top:160px;left:32px;right:32px}
  .story h2{color:var(--magenta);margin-bottom:10px}
  .story h3{color:var(--gold);margin:16px 0 6px}
  .story__band{position:absolute;left:0;right:0;bottom:0;height:40px;background:var(--magenta)}

  /* inside: right */
  .care{background:var(--gold);color:var(--white)}
  .care .photo{left:0;top:0;width:100%;height:330px}
  .care__body{position:absolute;top:350px;left:32px;right:30px}
  .care h2{margin-bottom:16px}
  .care .checklist li{font-size:12.5px}
  .care__band{position:absolute;left:0;right:0;bottom:0;height:40px;background:var(--magenta)}
</style>
</head>
<body>

<section class="spread spread--outside">
  <article class="panel flap">
    <div class="flap__body">
      <h2>Our New Programs</h2>
      <p>We are proud to share fresh ways for residents and families to stay active, healthy and close together.</p>
      <ul class="checklist">
        <li><svg width="16" height="16" viewBox="0 0 16 16"><circle cx="8" cy="8" r="8" fill="#a54499"/><path d="M4 8.5l2.5 2.5L12 5.5" stroke="#fff" stroke-width="2" fill="none"/></svg>Daily activities and outings</li>
        <li><svg width="16" height="16" viewBox="0 0 16 16"><circle cx="8" cy="8" r="8" fill="#a54499"/><path d="M4 8.5l2.5 2.5L12 5.5" stroke="#fff" stroke-width="2" fill="none"/></svg>New chef-made food recipes</li>
        <li><svg width="16" height="16" viewBox="0 0 16 16"><circle cx="8" cy="8" r="8" fill="#a54499"/><path d="M4 8.5l2.5 2.5L12 5.5" stroke="#fff" stroke-width="2" fill="none"/></svg>Physical and memory therapy</li>
        <li><svg width="16" height="16" viewBox="0 0 16 16"><circle cx="8" cy="8" r="8" fill="#a54499"/><path d="M4 8.5l2.5 2.5L12 5.5" stroke="#fff" stroke-width="2" fill="none"/></svg>Family and resident visits</li>
        <li><svg width="16" height="16" viewBox="0 0 16 16"><circle cx="8" cy="8" r="8" fill="#a54499"/><path d="M4 8.5l2.5 2.5L12 5.5" stroke="#fff" stroke-width="2" fill="none"/></svg>Covid-free safe community</li>
      </ul>
    </div>
    <svg class="photo" viewBox="0 0 367 300" preserveAspectRatio="none" role="img" aria-label="Photo of residents sharing a meal together">
      <defs><linearGradient id="gFlap" x1="0" y1="0" x2="1" y2="1"><stop offset="0" stop-color="#b9a79a"/><stop offset="1" stop-color="#6f5e58"/></linearGradient></defs>
      <path d="M0 40 Q183 0 367 40 V300 H0Z" fill="url(#gFlap)"/>
    </svg>
  </article>

  <article class="panel back">
    <div class="brand"><span class="brand__dot"></span>BRIGHTMOOR</div>
    <div class="brand-sub">SENIOR LIVING</div>
    <h2 class="back__title">Senior Living &amp; Memory Care</h2>
    <svg class="photo" viewBox="0 0 286 190" preserveAspectRatio="none" role="img" aria-label="Photo of the community building and garden">
      <defs><linearGradient id="gBack" x1="0" y1="0" x2="0" y2="1"><stop offset="0" stop-color="#b7c7d6"/><stop offset=".55" stop-color="#c9a278"/><stop offset="1" stop-color="#6f8a4e"/></linearGradient></defs>
      <rect width="286" height="190" fill="url(#gBack)"/>
    </svg>
    <div class="back__contact">
      <h2>Stay in Touch</h2>
      <div class="contact-line"><svg width="18" height="18" viewBox="0 0 24 24"><path d="M6.6 10.8a15 15 0 006.6 6.6l2.2-2.2a1 1 0 011-.25 11.4 11.4 0 003.6.6 1 1 0 011 1V20a1 1 0 01-1 1A17 17 0 013 4a1 1 0 011-1h3.5a1 1 0 011 1c0 1.25.2 2.45.6 3.6a1 1 0 01-.25 1z" fill="#fece3e"/></svg>(555) 014-2290</div>
      <div class="contact-line"><svg width="18" height="18" viewBox="0 0 24 24"><path d="M12 2a7 7 0 00-7 7c0 5.25 7 13 7 13s7-7.75 7-13a7 7 0 00-7-7zm0 9.5A2.5 2.5 0 1112 6.5a2.5 2.5 0 010 5z" fill="#fece3e"/></svg>4120 Harbor View Dr, Harbor Point</div>
      <div class="contact-line"><svg width="18" height="18" viewBox="0 0 24 24"><path d="M3 5h18v14H3z" fill="#fece3e"/><path d="M3 5l9 7 9-7" stroke="#a54499" stroke-width="2" fill="none"/></svg>hello@brightmoorliving.com</div>
    </div>
    <svg class="back__band" viewBox="0 0 367 120" preserveAspectRatio="none" aria-hidden="true">
      <path d="M0 40 Q183 0 367 40 V120 H0Z" fill="#c9a23d"/>
      <path d="M0 95 H367 V120 H0Z" fill="#8a3580"/>
    </svg>
  </article>

  <article class="panel cover">
    <div class="brand"><span class="brand__dot"></span>BRIGHTMOOR</div>
    <div class="brand-sub">SENIOR LIVING &amp; MEMORY CARE</div>
    <svg class="photo" viewBox="0 0 367 380" preserveAspectRatio="none" role="img" aria-label="Photo of a senior couple smiling on a patio">
      <defs><linearGradient id="gCover" x1="0" y1="0" x2="1" y2="1"><stop offset="0" stop-color="#c9b8a8"/><stop offset=".6" stop-color="#9c7f70"/><stop offset="1" stop-color="#6d5d55"/></linearGradient></defs>
      <rect width="367" height="380" fill="url(#gCover)"/>
    </svg>
    <svg class="cover__shape" viewBox="0 0 367 380" preserveAspectRatio="none" aria-hidden="true">
      <path d="M0 80 Q200 0 367 40 V380 H0Z" fill="#c9a23d"/>
      <path d="M0 90 Q200 10 367 50" stroke="#fff" stroke-width="4" fill="none"/>
      <path d="M0 330 H367 V380 H0Z" fill="#a54499"/>
    </svg>
    <div class="cover__tagline">Assisted Living<br>&amp; Memory Care</div>
    <div class="cover__subline">Harbor Point · Oak Hollow</div>
  </article>
</section>

<section class="spread spread--inside">
  <article class="panel programs">
    <div class="programs__list">
      <div class="program">
        <span class="program__icon"><svg width="16" height="16" viewBox="0 0 16 16"><path d="M3.5 8.5l3 3L13 5" stroke="#fff" stroke-width="2" fill="none"/></svg></span>
        <div><h3>Activities</h3><p>Music, art, games and outings fill each day with joy.</p></div>
      </div>
      <div class="program">
        <span class="program__icon"><svg width="16" height="16" viewBox="0 0 16 16"><path d="M3.5 8.5l3 3L13 5" stroke="#fff" stroke-width="2" fill="none"/></svg></span>
        <div><h3>Food Recipes</h3><p>Fresh seasonal menus made with care by our chefs.</p></div>
      </div>
      <div class="program">
        <span class="program__icon"><svg width="16" height="16" viewBox="0 0 16 16"><path d="M3.5 8.5l3 3L13 5" stroke="#fff" stroke-width="2" fill="none"/></svg></span>
        <div><h3>Therapy</h3><p>Gentle physical and memory programs for every resident.</p></div>
      </div>
      <div class="program">
        <span class="program__icon"><svg width="16" height="16" viewBox="0 0 16 16"><path d="M3.5 8.5l3 3L13 5" stroke="#fff" stroke-width="2" fill="none"/></svg></span>
        <div><h3>Family Time</h3><p>Safe visits and video calls keep loved ones close.</p></div>
      </div>
    </div>
    <svg class="photo" viewBox="0 0 367 300" preserveAspectRatio="none" role="img" aria-label="Photo of a caregiver with a smiling resident">
      <defs><linearGradient id="gProg" x1="0" y1="0" x2="1" y2="1"><stop offset="0" stop-color="#9fb8c4"/><stop offset="1" stop-color="#5a6f86"/></linearGradient></defs>
      <path d="M0 60 Q120 0 367 30 V300 H0Z" fill="url(#gProg)"/>
      <path d="M0 60 Q120 0 367 30" stroke="#fff" stroke-width="5" fill="none"/>
    </svg>
  </article>

  <article class="panel story">
    <div class="story__strip">
      <svg class="thumb" viewBox="0 0 10 10" preserveAspectRatio="none" role="img" aria-label="Photo of the dining room"><rect width="10" height="10" fill="#b08a6e"/></svg>
      <svg class="thumb" viewBox="0 0 10 10" preserveAspectRatio="none" role="img" aria-label="Photo of a resident lounge"><rect width="10" height="10" fill="#8f7a9a"/></svg>
      <svg class="thumb" viewBox="0 0 10 10" preserveAspectRatio="none" role="img" aria-label="Photo of the garden courtyard"><rect width="10" height="10" fill="#7f9368"/></svg>
    </div>
    <div class="story__body">
      <h2>Welcome Home</h2>
      <p>Brightmoor Senior Living offers warm assisted living and memory care in Harbor Point and Oak Hollow, where every resident is known by name.</p>
      <h3>Meet Our Manager</h3>
      <p>Our community manager brings years of senior care experience and a heart for family, leading a caring team day and night.</p>
      <h3>Covid-Free Care</h3>
      <p>Strict cleaning, screening and safe visit plans keep our residents, staff and families healthy and at ease.</p>
    </div>
    <div class="story__band"></div>
  </article>

  <article class="panel care">
    <svg class="photo" viewBox="0 0 367 330" preserveAspectRatio="none" role="img" aria-label="Photo of two seniors laughing outdoors">
      <defs><linearGradient id="gCare" x1="0" y1="0" x2="1" y2="1"><stop offset="0" stop-color="#a9c08a"/><stop offset="1" stop-color="#7b6a5d"/></linearGradient></defs>
      <path d="M0 0 H367 V280 Q200 340 0 300Z" fill="url(#gCare)"/>
      <path d="M0 300 Q200 340 367 280" stroke="#fff" stroke-width="5" fill="none"/>
    </svg>
    <div class="care__body">
      <h2>Our Services</h2>
      <ul class="checklist">
        <li><svg width="16" height="16" viewBox="0 0 16 16"><circle cx="8" cy="8" r="8" fill="#a54499"/><path d="M4 8.5l2.5 2.5L12 5.5" stroke="#fff" stroke-width="2" fill="none"/></svg>24-hour assisted living support</li>
        <li><svg width="16" height="16" viewBox="0 0 16 16"><circle cx="8" cy="8" r="8" fill="#a54499"/><path d="M4 8.5l2.5 2.5L12 5.5" stroke="#fff" stroke-width="2" fill="none"/></svg>Secure memory care suites</li>
        <li><svg width="16" height="16" viewBox="0 0 16 16"><circle cx="8" cy="8" r="8" fill="#a54499"/><path d="M4 8.5l2.5 2.5L12 5.5" stroke="#fff" stroke-width="2" fill="none"/></svg>Medication care and wellness</li>
        <li><svg width="16" height="16" viewBox="0 0 16 16"><circle cx="8" cy="8" r="8" fill="#a54499"/><path d="M4 8.5l2.5 2.5L12 5.5" stroke="#fff" stroke-width="2" fill="none"/></svg>Housekeeping and laundry</li>
        <li><svg width="16" height="16" viewBox="0 0 16 16"><circle cx="8" cy="8" r="8" fill="#a54499"/><path d="M4 8.5l2.5 2.5L12 5.5" stroke="#fff" stroke-width="2" fill="none"/></svg>Tours open every day</li>
      </ul>
    </div>
    <div class="care__band"></div>
  </article>
</section>

</body>
</html>
```